Need a Shopvantro Design for a new company called DeskMarlow

DeskMarlow is a new US company that sells compatible toner cartridges and remanufactured ink jet cartridges and other office supplies direct from the manufacturers. We will need to add an app like Kit Locator to the site so that users can search for supplies for their machine model. We need to connect our Zephora and quilo inventory with the ShopVantro site through Stockwisp.

```html
<!DOCTYPE html>
<html lang="en">
<head>
<meta charset="utf-8">
<title>DeskMarlow – Office Supplies</title>
<link href="https://fonts.googleapis.com/css2?family=Quicksand:wght@400;500;600;700&family=Arimo:wght@400;700&display=swap" rel="stylesheet">
<style>
:root{
  --blue:#1b9ae4;
  --magenta:#e5157f;
  --yellow:#fdf200;
  --dark:#1f1f1f;
  --topbar:#222222;
  --text:#333333;
  --muted:#666666;
  --star:#f7941d;
  --price:#c8136f;
  --line:#e6e6e6;
  --soft:#f4f4f4;
}
*{box-sizing:border-box;margin:0;padding:0}
html,body{width:1200px;height:3267px;overflow:hidden}
body{position:relative;background:#fff;font-family:"Arimo",Arial,sans-serif;color:var(--text)}
.section{position:absolute;left:0;width:1200px}
.container{position:absolute;left:112px;width:976px}
.heading{position:absolute;left:0;width:1200px;text-align:center;font-family:"Quicksand",sans-serif;font-weight:500;font-size:36px;color:#222}
.heading::after{content:"";display:block;width:46px;height:3px;background:var(--blue);margin:16px auto 0}

/* top bar */
.topbar{top:0;height:52px;background:var(--topbar)}
.topbar ul{position:absolute;right:112px;top:0;height:52px;display:flex;gap:26px;list-style:none;align-items:center}
.topbar li{font-family:"Quicksand",sans-serif;font-weight:600;font-size:12px;color:#fff;display:flex;align-items:center;gap:7px;letter-spacing:.2px}
.topbar svg{width:12px;height:12px;fill:#fff}

/* header */
.header{top:52px;height:133px}
.social{position:absolute;left:112px;top:58px;display:flex;gap:6px}
.social span{width:33px;height:33px;border:1.5px solid #444;border-radius:50%}
.brand{position:absolute;left:446px;top:42px;display:flex;align-items:center;gap:12px}
.brand-dot{width:56px;height:56px;border-radius:50%;background:var(--dark)}
.brand-name{font-family:"Quicksand",sans-serif;font-weight:700;font-size:31px;color:#111;letter-spacing:1.5px}
.search{position:absolute;left:807px;top:52px;width:281px;height:43px;border:1.5px solid #ccc;border-radius:3px;font-family:"Quicksand",sans-serif;font-size:16px;color:#444;padding:11px 14px}
.search svg{position:absolute;right:14px;top:14px;width:13px;height:13px}

/* nav */
.nav{top:185px;height:62px;background:var(--blue);border-bottom:3px solid #fff}
.nav ul{list-style:none;display:flex;justify-content:center;gap:77px;padding-top:22px}
.nav li{font-family:"Quicksand",sans-serif;font-weight:500;font-size:15px;color:#fff}

/* hero */
.hero{top:250px;height:680px;background:radial-gradient(ellipse at 60% 45%,#5a5a5a 0%,#2e2e2e 55%,#161616 100%)}
.hero h1{position:absolute;top:205px;width:100%;text-align:center;font-family:"Quicksand",sans-serif;font-weight:500;font-size:82px;color:#fff}
.hero p{position:absolute;top:312px;left:200px;width:800px;text-align:center;font-family:"Quicksand",sans-serif;font-weight:500;font-size:25px;line-height:38px;color:#fff}
.btn-shop{position:absolute;left:504px;top:412px;width:192px;height:58px;background:var(--blue);border-radius:3px;color:#fff;font-family:"Quicksand",sans-serif;font-weight:700;font-size:19px;text-align:center;line-height:58px}

/* categories */
.categories{top:1074px;height:310px}
.cat{position:absolute;top:0;width:314px;height:310px}
.cat-img{height:245px}
.cat-label{height:65px;text-align:center;line-height:65px;font-family:"Quicksand",sans-serif;font-weight:500;font-size:23px;color:#fff}
.cat-toner .cat-img{background:linear-gradient(135deg,#3a3a3a,#9e9e3c 35%,#c83d85 55%,#2a6cb0 75%,#1a1a1a)}
.cat-inkjet .cat-img{background:linear-gradient(180deg,#2a2e35,#6f7680 50%,#1d2025)}
.cat-other .cat-img{background:linear-gradient(160deg,#1c1c1c,#5a5a5a 45%,#262626)}
.cat-toner .cat-label{background:var(--blue)}
.cat-inkjet .cat-label{background:var(--magenta)}
.cat-other .cat-label{background:var(--yellow);color:#222}

/* products */
.products{height:288px}
.product{position:absolute;top:0;width:235px;height:288px;border:1px solid var(--line);box-shadow:0 0 4px rgba(0,0,0,.08);text-align:center}
.product-img{position:absolute;left:15px;top:12px;width:205px;height:155px;border-radius:4px}
.stars{position:absolute;top:182px;width:100%;color:var(--star);font-size:13px;letter-spacing:1px}
.product-name{position:absolute;top:200px;width:100%;font-family:"Quicksand",sans-serif;font-weight:500;font-size:19px;color:#333}
.price{position:absolute;top:232px;width:100%;font-family:"Quicksand",sans-serif;font-weight:600;font-size:19px;color:var(--price)}
.tone-a{background:linear-gradient(90deg,#2bb3d8,#d83a9a,#e8d53a,#333)}
.tone-b{background:linear-gradient(90deg,#222,#3aa8d8 40%,#d83a8a 60%,#f0dc2a)}
.tone-c{background:linear-gradient(180deg,#e05a9a,#333 30%,#e8d53a 55%,#333 70%,#3ab0e0)}
.tone-d{background:linear-gradient(135deg,#fff,#d83a7a 40%,#222 60%,#f07c2a 85%,#fff)}
.tone-e{background:linear-gradient(90deg,#2a6ab0,#c83a4a,#e0a030,#333)}
.tone-f{background:linear-gradient(120deg,#f0dc2a,#222 40%,#e04a9a 70%,#444)}
.tone-g{background:linear-gradient(180deg,#f0dc2a,#333 40%,#7a2a4a 70%,#d05a2a)}
.tone-h{background:linear-gradient(90deg,#222,#3a6ae0 40%,#e0407a 70%,#c8a020)}

/* posts */
.posts-bg{top:2362px;height:566px;background:var(--soft)}
.post{position:absolute;top:2507px;width:235px;text-align:center}
.post-img{height:180px}
.post-date{margin-top:23px;font-family:"Quicksand",sans-serif;font-weight:500;font-size:17px}
.post-title{margin-top:9px;font-family:"Quicksand",sans-serif;font-weight:500;font-size:20px;color:#333}
.post-text{margin-top:14px;font-size:13px;line-height:24px;color:var(--muted)}
.read-more{display:inline-block;margin-top:12px;width:104px;height:37px;line-height:35px;border:1.5px solid;font-size:14px;background:#fff}
.post.blue .post-date,.post.blue .read-more{color:var(--blue);border-color:var(--blue)}
.post.pink .post-date,.post.pink .read-more{color:var(--magenta);border-color:var(--magenta)}
.pi-1{background:linear-gradient(135deg,#3a2a1a,#d8a03a 30%,#3ab0d8 55%,#222)}
.pi-2{background:linear-gradient(160deg,#e0e0e0,#3a3a3a 45%,#888)}
.pi-3{background:linear-gradient(150deg,#444,#e0c83a 40%,#d04a8a 60%,#3a9ad8 80%,#222)}
.pi-4{background:linear-gradient(170deg,#222,#e0d03a 35%,#3a8ad8 60%,#c03a6a 85%,#222)}

/* footer */
.footer{top:2928px;height:339px;background:var(--dark);color:#fff}
.fcol{position:absolute;top:56px}
.fcol h4{font-family:"Arimo",sans-serif;font-weight:700;font-size:15px;letter-spacing:.3px;margin-bottom:20px}
.fcol ul{list-style:none}
.fcol li{font-size:12.5px;line-height:26px;position:relative;padding-left:27px}
.fcol li::before{content:"";position:absolute;left:3px;top:9px;border-left:5px solid #fff;border-top:4px solid transparent;border-bottom:4px solid transparent}
.stores li{padding-left:29px;font-size:11px;line-height:14px;margin-bottom:15px}
.stores li::before{display:none}
.stores svg{position:absolute;left:0;top:0;width:13px;height:13px;fill:#fff}
.stores a{color:#fff}
.news p{font-size:11px;line-height:14px;margin-bottom:14px;width:160px}
.email{width:161px;height:38px;background:#fff;border-radius:3px;color:#555;font-size:11px;padding:12px 16px;position:relative}
.email svg{position:absolute;right:12px;top:12px;width:13px;height:13px;fill:var(--blue)}
.copyright{position:absolute;top:302px;width:100%;text-align:center;font-size:12.5px}
</style>
</head>
<body>

<div class="section topbar">
  <ul>
    <li><svg viewBox="0 0 12 12"><rect x="1" y="4" width="10" height="3"/><rect x="2" y="7" width="8" height="5"/><rect x="5.2" y="3" width="1.6" height="9" fill="#222"/></svg>GIFT CERTIFICATES</li>
    <li><svg viewBox="0 0 12 12"><circle cx="6" cy="3.5" r="3"/><path d="M0 12c0-4 3-5.5 6-5.5s6 1.5 6 5.5z"/></svg>SIGN IN OR REGISTER</li>
    <li><svg viewBox="0 0 12 12"><path d="M6 11 1 6a3 3 0 0 1 5-3.5A3 3 0 0 1 11 6z"/></svg>WISH LISTS</li>
    <li><svg viewBox="0 0 12 12"><path d="M0 1h2l2 7h7l1-5H3.5"/><circle cx="5" cy="10.5" r="1.2"/><circle cx="10" cy="10.5" r="1.2"/></svg>CART 0</li>
  </ul>
</div>

<div class="section header">
  <div class="social"><span></span><span></span><span></span><span></span><span></span></div>
  <div class="brand"><span class="brand-dot"></span><span class="brand-name">DESKMARLOW</span></div>
  <div class="search">Search
    <svg viewBox="0 0 13 13" fill="none" stroke="#333" stroke-width="2"><circle cx="5.5" cy="5.5" r="4"/><path d="M8.5 8.5 12 12"/></svg>
  </div>
</div>

<nav class="section nav">
  <ul><li>HOME</li><li>ABOUT US</li><li>SERVICES</li><li>PRODUCTS</li><li>NEWS</li><li>CONTACT US</li></ul>
</nav>

<div class="section hero" role="img" aria-label="Close-up of ink cartridges installed in a printer">
  <h1>DeskMarlow</h1>
  <p>Sed ut perspiciatis unde omnis iste natus error sit voluptatem accusantium doloremque laudantium</p>
  <div class="btn-shop">SHOP NOW</div>
</div>

<h2 class="heading" style="top:983px">Featured Categories</h2>
<div class="container categories">
  <div class="cat cat-toner" style="left:0"><div class="cat-img" role="img" aria-label="Colour toner cartridges laid on a table"></div><div class="cat-label">Toner Cartridges</div></div>
  <div class="cat cat-inkjet" style="left:331px"><div class="cat-img" role="img" aria-label="Colour and black inkjet cartridges in a printer carriage"></div><div class="cat-label">Inkjet Cartridges</div></div>
  <div class="cat cat-other" style="left:662px"><div class="cat-img" role="img" aria-label="Row of ink tanks inside a printer"></div><div class="cat-label">Other</div></div>
</div>

<h2 class="heading" style="top:1464px">Featured Products</h2>
<div class="container products" style="top:1556px">
  <div class="product" style="left:0"><div class="product-img tone-a" role="img" aria-label="Set of four toner cartridges"></div><div class="stars">★★★★★</div><div class="product-name">Product Name</div><div class="price">£30.00</div></div>
  <div class="product" style="left:247px"><div class="product-img tone-b" role="img" aria-label="Stacked colour toner cartridges"></div><div class="stars">★★★★★</div><div class="product-name">Product Name</div><div class="price">£30.00</div></div>
  <div class="product" style="left:494px"><div class="product-img tone-c" role="img" aria-label="Stack of laser toner cartridges"></div><div class="stars">★★★★★</div><div class="product-name">Product Name</div><div class="price">£30.00</div></div>
  <div class="product" style="left:741px"><div class="product-img tone-d" role="img" aria-label="Single magenta toner cartridge"></div><div class="stars">★★★★★</div><div class="product-name">Product Name</div><div class="price">£30.00</div></div>
</div>

<h2 class="heading" style="top:1912px">New Products</h2>
<div class="container products" style="top:2004px">
  <div class="product" style="left:0"><div class="product-img tone-e" role="img" aria-label="Four inkjet cartridges in a row"></div><div class="stars">★★★★★</div><div class="product-name">Product Name</div><div class="price">£30.00</div></div>
  <div class="product" style="left:247px"><div class="product-img tone-f" role="img" aria-label="Yellow and magenta inkjet cartridges"></div><div class="stars">★★★★★</div><div class="product-name">Product Name</div><div class="price">£30.00</div></div>
  <div class="product" style="left:494px"><div class="product-img tone-g" role="img" aria-label="Two printhead cartridges"></div><div class="stars">★★★★★</div><div class="product-name">Product Name</div><div class="price">£30.00</div></div>
  <div class="product" style="left:741px"><div class="product-img tone-h" role="img" aria-label="Refill ink bottles"></div><div class="stars">★★★★★</div><div class="product-name">Product Name</div><div class="price">£30.00</div></div>
</div>

<div class="section posts-bg"></div>
<h2 class="heading" style="top:2409px">Recent Posts</h2>
<div class="post blue" style="left:112px"><div class="post-img pi-1" role="img" aria-label="Ink cartridges close-up"></div><div class="post-date">22nd Feb 2021</div><div class="post-title">Sed ut perspiciatis</div><div class="post-text">Nemo enim ipsam voluptatem quia voluptas sit aspernatur aut</div><span class="read-more">Read More</span></div>
<div class="post pink" style="left:360px"><div class="post-img pi-2" role="img" aria-label="Cartridges inside a printer"></div><div class="post-date">22nd Feb 2021</div><div class="post-title">Sed ut perspiciatis</div><div class="post-text">Nemo enim ipsam voluptatem quia voluptas sit aspernatur aut</div><span class="read-more">Read More</span></div>
<div class="post blue" style="left:607px"><div class="post-img pi-3" role="img" aria-label="Hand fitting a toner cartridge"></div><div class="post-date">22nd Feb 2021</div><div class="post-title">Sed ut perspiciatis</div><div class="post-text">Nemo enim ipsam voluptatem quia voluptas sit aspernatur aut</div><span class="read-more">Read More</span></div>
<div class="post pink" style="left:855px"><div class="post-img pi-4" role="img" aria-label="Hand removing a toner cartridge from a printer"></div><div class="post-date">22nd Feb 2021</div><div class="post-title">Sed ut perspiciatis</div><div class="post-text">Nemo enim ipsam voluptatem quia voluptas sit aspernatur aut</div><span class="read-more">Read More</span></div>

<footer class="section footer">
  <div class="fcol" style="left:110px"><h4>INFORMATION</h4><ul><li>Shipping Policy</li><li>Refund &amp; Returns Policy</li><li>Privacy Policy</li><li>Contact Us</li><li>Sitemap</li></ul></div>
  <div class="fcol" style="left:322px"><h4>WHY CHOOSE US</h4><ul><li>Sed ut perspiciatis</li><li>unde omnis iste</li><li>natus error sit</li><li>voluptatem</li><li>accusantium</li><li>natus error sit</li></ul></div>
  <div class="fcol" style="left:511px"><h4>CATEGORIES</h4><ul><li>March Madness!</li><li>Bollards</li><li>Car Park Management</li><li>Wheel Stops</li><li>Traffic Management</li><li>Convex Mirrors and Dome</li></ul></div>
  <div class="fcol stores" style="left:724px;top:58px"><h4>STORES</h4><ul>
    <li><svg viewBox="0 0 13 13"><path d="M1 5c0-2 2-3 5.5-3S12 3 12 5v1H9V5H4v1H1z"/><rect x="2" y="7" width="9" height="5" rx="1"/></svg>000-121-1231 (Phone)</li>
    <li><svg viewBox="0 0 13 13"><rect x="3" y="0" width="7" height="4"/><rect x="0" y="4" width="13" height="6" rx="1"/><rect x="3" y="8" width="7" height="5" fill="#fff" stroke="#1f1f1f"/></svg>000-121-1231 &nbsp;(Fax)</li>
    <li><svg viewBox="0 0 13 13"><rect x="0" y="2" width="13" height="9"/><path d="M0 2l6.5 5L13 2" fill="none" stroke="#1f1f1f"/></svg><a>info@deskmarlow.com</a></li>
    <li><svg viewBox="0 0 13 13"><path d="M6.5 0a4.5 4.5 0 0 1 4.5 4.5C11 8 6.5 13 6.5 13S2 8 2 4.5A4.5 4.5 0 0 1 6.5 0z"/><circle cx="6.5" cy="4.5" r="1.6" fill="#1f1f1f"/></svg># 244 Lorem Ipsum Dummy Text Lorem</li>
  </ul></div>
  <div class="fcol news" style="left:927px;top:58px"><h4>NEWSLETTER</h4><p>Get the latest updates on new products and upcoming sales</p>
    <div class="email">Email :<svg viewBox="0 0 13 13"><path d="M0 6 13 0 10 13 6 8z"/></svg></div></div>
  <div class="copyright">© Copyright 2021 DeskMarlow .All Rights Reserved</div>
</footer>

</body>
</html>
```